Design a Mobile App for Landscape Businesses

This project is to design the first three screens for a mobile app for Landscape and Lawncare businesses. This app will serve as a directory for homeowners to locate landscape and lawn care businesses and for landscape businesses and contractors to run their business. See the attached PDF for more information and example
Here is the link to the description https://brevlinq.test/k3r92P

Target Market(s)

Landscape and lawn care business, gardeners, home owners

Industry/Entity Type

Landscape Gardening

Logo Text

Quillmoray

Colors

Designer to choose colors to be used in the design.

```html
<!DOCTYPE html>
<html lang="en">
<head>
<meta charset="utf-8">
<title>Quillmoray – Edit Profile</title>
<link href="https://fonts.googleapis.com/css2?family=Montserrat:wght@400;500;600&display=swap" rel="stylesheet">
<style>
  :root {
    --canvas: #e7e7e3;
    --screen: #f4f4f2;
    --green: #6b8412;
    --green-dark: #5c7210;
    --chip-light: #a7b67a;
    --field: #e9e9e5;
    --label: #8e8e8a;
    --ink: #2f2f2d;
    --white: #ffffff;
    --remove: #e0363a;
  }
  * { box-sizing: border-box; margin: 0; padding: 0; }
  html, body {
    width: 1200px; height: 983px; overflow: hidden;
    background: var(--canvas);
    font-family: "Montserrat", sans-serif;
    color: var(--ink);
  }
  .screen {
    position: absolute; left: 360px; top: 38px;
    width: 480px; height: 906px;
    background: var(--screen);
    overflow: hidden;
    box-shadow: 0 10px 40px rgba(0,0,0,.12);
  }
  .app-header { background: var(--green); color: var(--white); height: 120px; }
  .status-bar {
    display: flex; align-items: center; justify-content: space-between;
    height: 34px; padding: 0 16px; font-size: 13px; opacity: .9;
  }
  .status-left, .status-right { display: flex; align-items: center; gap: 6px; }
  .signal { display: flex; gap: 3px; }
  .signal span { width: 6px; height: 6px; border-radius: 50%; background: var(--white); }
  .signal span.off { background: transparent; border: 1px solid var(--white); }
  .battery { width: 30px; height: 12px; border: 1px solid var(--white); border-radius: 2px; padding: 1px; }
  .battery i { display: block; width: 100%; height: 100%; background: var(--white); }
  .title-bar { position: relative; height: 86px; display: flex; align-items: center; justify-content: center; }
  .title-bar h1 { font-size: 20px; font-weight: 600; }
  .back { position: absolute; left: 20px; top: 30px; }

  .profile-form { padding: 18px 30px 0; }
  .field { margin-bottom: 14px; }
  .field label { display: block; font-size: 11px; color: var(--label); margin: 0 0 5px 14px; }
  .input {
    height: 46px; border-radius: 23px; background: var(--field);
    display: flex; align-items: center; justify-content: space-between;
    padding: 0 20px; font-size: 15px; color: var(--ink);
    border: 1px solid #e0e0db;
  }
  .textarea { height: 140px; border-radius: 22px; align-items: flex-start; }
  .row { display: flex; gap: 18px; }
  .row .field { flex: 1; }

  .chips { display: flex; flex-wrap: wrap; gap: 14px 22px; align-items: center; padding: 4px 0 6px; }
  .chip {
    position: relative; height: 32px; padding: 0 22px; border-radius: 16px;
    display: inline-flex; align-items: center; font-size: 12px; font-weight: 500; color: var(--white);
  }
  .chip.selected { background: var(--green); }
  .chip.suggested { background: var(--chip-light); }
  .chip .badge {
    position: absolute; right: -9px; top: 50%; transform: translateY(-50%);
    width: 18px; height: 18px; border-radius: 50%;
    display: flex; align-items: center; justify-content: center;
  }
  .badge.remove { background: var(--remove); }
  .badge.add { background: var(--green-dark); border: 1.5px solid var(--white); }
  .add-offering { width: 20px; height: 20px; }

  .social-row { display: flex; gap: 18px; align-items: flex-end; margin-top: 8px; }
  .social-row .field { flex: 1.4; margin-bottom: 0; }
  .btn {
    border: none; background: var(--green); color: var(--white);
    font-family: "Montserrat", sans-serif; font-size: 16px; font-weight: 500;
    display: flex; align-items: center; justify-content: center;
  }
  .btn-connect { flex: 1; height: 46px; border-radius: 23px; }
  .btn-update { width: 100%; height: 62px; border-radius: 31px; font-size: 20px; margin-top: 26px; }
</style>
</head>
<body>
<main class="screen">
  <header class="app-header">
    <div class="status-bar">
      <div class="status-left">
        <div class="signal"><span></span><span></span><span></span><span class="off"></span><span class="off"></span></div>
        <span>FFF</span>
        <svg width="14" height="11" viewBox="0 0 14 11"><path d="M7 10 L1 4 A8.5 8.5 0 0 1 13 4 Z" fill="#fff"/></svg>
      </div>
      <div class="status-right">
        <svg width="11" height="11" viewBox="0 0 11 11"><circle cx="5.5" cy="5.5" r="4.5" fill="none" stroke="#fff"/><path d="M5.5 3v3l2 1" stroke="#fff" fill="none"/></svg>
        <span>100%</span>
        <div class="battery"><i></i></div>
      </div>
    </div>
    <div class="title-bar">
      <svg class="back" width="24" height="18" viewBox="0 0 24 18"><path d="M23 9H3M10 2L3 9l7 7" stroke="#fff" stroke-width="2.6" fill="none" stroke-linecap="round" stroke-linejoin="round"/></svg>
      <h1>Edit Profile</h1>
    </div>
  </header>

  <form class="profile-form">
    <div class="field"><label>Business Name</label><div class="input">Marlowe Gardens</div></div>
    <div class="field"><label>Address</label><div class="input">48 Ferncliff Avenue</div></div>
    <div class="row">
      <div class="field"><label>City</label><div class="input">Sacramento</div></div>
      <div class="field"><label>Zip Code</label><div class="input">90002</div></div>
    </div>
    <div class="field"><label>State</label><div class="input">California
      <svg width="12" height="8" viewBox="0 0 12 8"><path d="M1 1l5 5 5-5" stroke="#555" stroke-width="1.5" fill="none"/></svg></div></div>
    <div class="field"><label>Mobile Number</label><div class="input">(555) 210-384</div></div>
    <div class="field"><label>Company Info</label><div class="input textarea"></div></div>

    <div class="field">
      <label>Service Offerings</label>
      <div class="chips">
        <span class="chip suggested">Patios<span class="badge remove"><svg width="8" height="2"><rect width="8" height="2" fill="#fff"/></svg></span></span>
        <svg class="add-offering" viewBox="0 0 20 20"><circle cx="10" cy="10" r="8" fill="none" stroke="#333" stroke-width="1.4"/><path d="M10 6v8M6 10h8" stroke="#333" stroke-width="1.4"/></svg>
        <span class="chip selected">Walkways<span class="badge add"><svg width="8" height="8"><path d="M4 0v8M0 4h8" stroke="#fff" stroke-width="2"/></svg></span></span>
        <span class="chip suggested">Interlocking<span class="badge remove"><svg width="8" height="2"><rect width="8" height="2" fill="#fff"/></svg></span></span>
        <span class="chip suggested">Landscaping<span class="badge remove"><svg width="8" height="2"><rect width="8" height="2" fill="#fff"/></svg></span></span>
        <span class="chip selected">Lawn Care</span>
      </div>
    </div>

    <div class="social-row">
      <div class="field"><label>Social Connect</label><div class="input">Chirpnet
        <svg width="12" height="8" viewBox="0 0 12 8"><path d="M1 1l5 5 5-5" stroke="#555" stroke-width="1.5" fill="none"/></svg></div></div>
      <button type="button" class="btn btn-connect">Connect</button>
    </div>

    <button type="button" class="btn btn-update">Update</button>
  </form>
</main>
</body>
</html>
```